Divorce marketing brochure - Which will include a toy ball and chain as a gimick

A single page marketing enclosure which includes a toy ball and chain to be given to lawyers. I want to convey the following messages:

1. We pay a 1/3 referral fee;
2. We solve difficult problems.

Examples of problems solved:
*Litigation of complex property, custody, support and parenting time issues;
*Protection (or invasion) of personal injury proceeds in divorce;
*Distribution of consortium proceeds in divorce;
*Pre-nuptial and Post-nuptial agreements.
*Settlements
*Reduce conflict

A sample of the toy ball and chain enclosure can be viewed here:

My website is www.thesplitcounsel.com (currently being updated - who's isn't?)

http://www.shopvarnex.com/Pelbrook-Gadgets-Inc-Convict-Shackle/dp/Q7K4TZ2MXA/ref=sr_1_9?ie=UTF8&qid=1311011554&sr=8-9

Target Market(s)

Personal Injury Attorneys

Industry/Entity Type

Marketing

Requirements
Must have
• Call to action:

www.thesplitcounsel.com
1-866-LAWS-DESK
517-624-8107
Marcus@brevanolegal.com
Nice to have
• I want this campaign to stand out. Different is good. I am a divorce lawyer marketing to personal injury attorneys (and some others) for divorce referrals. (No one forgets the girl with red hair and braces) I want the campaign to be remembered without being offensive.
Should not have

```html
<!DOCTYPE html>
<html lang="en">
<head>
<meta charset="utf-8">
<title>Choosing the right divorce attorney</title>
<link rel="stylesheet" href="https://fonts.googleapis.com/css2?family=Arimo:wght@700&family=PT+Sans:wght@400;700&display=swap">
<style>
  :root {
    --navy: #0d3a78;
    --navy-deep: #0a2f66;
    --title-blue: #164a8c;
    --sky-top: #c9d0e3;
    --sky-bottom: #eef0f6;
    --grey-wave: #9a9ca6;
    --pale: #e8e9ee;
    --badge: #7180b3;
    --white: #ffffff;
  }
  html, body { margin: 0; padding: 0; overflow: hidden; }
  body { width: 849px; height: 1200px; background: var(--white); }
  .brochure {
    position: relative; width: 849px; height: 1200px; overflow: hidden;
    background: linear-gradient(180deg, var(--sky-top) 0%, var(--sky-bottom) 45%, #f4f5f9 60%);
    font-family: "PT Sans", sans-serif;
  }
  .backdrop { position: absolute; inset: 0; }
  .top-bar { position: absolute; top: 0; left: 95px; right: 0; height: 32px; background: var(--navy); }
  .headline { position: absolute; left: 100px; top: 80px; margin: 0; font-family: "Arimo", sans-serif; font-weight: 700; }
  .headline .lead { display: block; color: var(--white); font-size: 46px; line-height: 1.1; }
  .headline .main { display: block; color: var(--title-blue); font-size: 73px; line-height: 1.05; letter-spacing: -0.5px; }
  .intro { position: absolute; left: 212px; top: 240px; width: 600px; color: var(--navy); }
  .intro h2 { margin: 0 0 8px; font-family: "Arimo", sans-serif; font-size: 28px; color: var(--title-blue); }
  .intro p { margin: 0; font-size: 20.5px; line-height: 32.5px; }
  .intro .indent-1 { padding-left: 98px; }
  .intro .indent-2 { padding-left: 119px; }
  .badge {
    position: absolute; border-radius: 50%; background: var(--badge);
    color: var(--white); font-family: "Arimo", sans-serif; font-weight: 700;
    display: flex; align-items: center; justify-content: center; text-align: center;
    box-shadow: 2px 3px 8px rgba(0,0,0,0.35);
  }
  .badge-referral { left: 155px; top: 525px; width: 216px; height: 216px; font-size: 27px; line-height: 1.08; }
  .badge-solve { left: 610px; top: 918px; width: 206px; height: 206px; font-size: 31px; line-height: 1.12; }
  .services { position: absolute; left: 388px; top: 630px; color: var(--white); }
  .services h3 { margin: 0 0 8px 8px; font-family: "Arimo", sans-serif; font-size: 29px; color: var(--white); }
  .services ul { margin: 0; padding: 0; list-style: none; font-weight: 700; font-size: 19px; line-height: 25.5px; }
  .services li { padding-left: 16px; text-indent: -10px; }
  .services li::before { content: "• "; }
  .services .cont { display: block; text-indent: 0; padding-left: 4px; }
  .contact { position: absolute; left: 71px; top: 1062px; color: var(--navy); }
  .contact h4 { margin: 0 0 10px; font-family: "Arimo", sans-serif; font-size: 29px; }
  .contact p { margin: 0; font-size: 17px; line-height: 28px; }
  .website { position: absolute; right: 50px; top: 1150px; margin: 0; color: var(--white); font-weight: 700; font-size: 20px; }
</style>
</head>
<body>
<main class="brochure">
  <svg class="backdrop" width="849" height="1200" viewBox="0 0 849 1200" aria-hidden="true">
    <defs>
      <linearGradient id="navyFill" x1="0" y1="0" x2="0" y2="1">
        <stop offset="0" stop-color="#123f80"/>
        <stop offset="1" stop-color="#0a2f66"/>
      </linearGradient>
      <radialGradient id="artFill" cx="0.45" cy="0.5" r="0.6">
        <stop offset="0" stop-color="#8ea8dc"/>
        <stop offset="0.6" stop-color="#6a7fae" stop-opacity="0.8"/>
        <stop offset="1" stop-color="#3a3f4a" stop-opacity="0"/>
      </radialGradient>
    </defs>
    <path d="M0,610 C230,520 520,470 849,440 L849,1200 L0,1200 Z" fill="#b9bcc6"/>
    <path d="M0,640 C260,560 520,525 849,500 L849,1200 L0,1200 Z" fill="var(--grey-wave)"/>
    <path d="M0,700 C280,600 540,560 849,535 L849,1200 L0,1200 Z" fill="url(#navyFill)"/>
    <path d="M380,690 C560,630 700,620 849,650 L849,690 C700,660 560,670 380,720 Z" fill="#8d909b" opacity="0.7"/>
    <path d="M0,1020 C170,975 420,990 560,1200 L0,1200 Z" fill="var(--pale)"/>
    <rect x="0" y="420" width="380" height="640" rx="60" fill="url(#artFill)" role="img" aria-label="Illustration of a blue figure breaking free from a ball and chain"/>
  </svg>

  <div class="top-bar"></div>

  <h1 class="headline">
    <span class="lead">Choosing the right</span>
    <span class="main">divorce attorney</span>
  </h1>

  <section class="intro">
    <h2>Are you planning a divorce?</h2>
    <p>Divorce is stressful for most, for some it is a relief.<br>
    A person will usually experience some form of<br>
    denial, shock and confusion before being able<br>
    to let go of the relationship. Unfortunately, in<br>
    addition to navigating the emotional component</p>
    <p class="indent-1">of a divorce, you must also choose</p>
    <p class="indent-2">an attorney.</p>
  </section>

  <div class="badge badge-referral">We pay<br>a 1/3<br>referral fee;</div>

  <section class="services">
    <h3>We deal with...</h3>
    <ul>
      <li>Litigation of complex property,<span class="cont">custody, support and parenting</span><span class="cont">time issues;</span></li>
      <li>Protection (or invasion) of personal<span class="cont">injury proceeds in divorce;</span></li>
      <li>Distribution of consortium proceeds<span class="cont">in divorce;</span></li>
      <li>Pre-nuptial and Post-nuptial agreements.</li>
      <li>Settlements</li>
      <li>Reduce conflict</li>
    </ul>
  </section>

  <div class="badge badge-solve">We solve<br>difficult<br>problems.</div>

  <section class="contact">
    <h4>Call now</h4>
    <p>1-866-LAWS-DESK</p>
    <p>t : 517-624-8107 - Marcus@brevanolegal.com</p>
  </section>

  <p class="website">www.thesplitcounsel.com</p>
</main>
</body>
</html>
```